Business Card - high end, modern health care

Hey designers!

We need a double sided business card for the boutique, cutting edge physical therapy rehabilitation centre in Sydney's Northern Beaches.

With the most qualified physios in the area The Harbourline Motion Clinic does what other physiotherapy practices do not, we take our time with our patients giving them longer appointments, better physios and therefor faster results!

We guarantee that the service people receive at THMC will be unparalleled.

Hence we need a business card to reflect our modern, boutique, high end service. The final design needs to reflect that we are in a class of our own yet with the feel of beachside retreat.

Below I have attached our logo in both blue on white and white on blue. The exact colour is;
and the font that we have used in our logo is Tex Gyre Aventador.

I like the idea of the blue as the main colour as it is more eye catching and our signage onto the main road will be in this blue and in the interest of consistency across marketing the blue needs to be a part of the design. However I would appreciate a few designs onto a wooden background as this is a visual theme within the fitout of the practice.

The design needs to be of standard size (91x55mm).

Target Market(s)

We target people who have an end outcome in mind and those who have had poor experiences with other providers and ensure that everyone gets the care that they deserve with a premium service that is tailored to the individuals circumstances. As a premium service, the target market is highly educated, business and tech savvy with the additional target market of elderly people who have self funded their retirement and see value in paying for the best ongoing rehabilitation to maintain independence.

Industry/Entity Type

Physical Therapy

Contact Information for Business Card

Name, designation( Titled Musculoskeletal Physiotherapist... there will also be those in the company that have multiple designations ie 5 or 6 words long), phone number, email, facebook, instagram, address

Font styles to use
Sans Serif

Colors

Designer to choose colors to be used in the design.

Requirements
Must have
• Front - The logo as large as possible, blue or wooden theme, and all of the important details.
• Back - A blank space/lines on which to write appointment times (no "Appointment, date, time" etc.)
Nice to have
• facebook url
• logos for facebook and instagram
• Mini logos for the phone and email?

```html
<!DOCTYPE html>
<html lang="en">
<head>
<meta charset="utf-8">
<title>The Harbourline Motion Clinic – Business Card</title>
<link rel="stylesheet" href="https://fonts.googleapis.com/css2?family=Lato:wght@400;700&display=swap">
<style>
  :root {
    --stage: #4a423d;
    --card: #0c0c0c;
    --brand-blue: #1f6cc4;
    --ink-light: #f2f2f2;
    --ink-muted: #cfcfcf;
    --silver: #d9d9d9;
    --band: #e6e6e6;
    --band-ink: #111111;
    --rule: #3a3a3a;
  }
  * { box-sizing: border-box; margin: 0; padding: 0; }
  html, body {
    width: 1200px; height: 900px; overflow: hidden;
    background: var(--stage);
    font-family: "Lato", sans-serif;
  }
  .canvas {
    width: 1200px; height: 900px;
    display: flex; align-items: center; justify-content: center; gap: 60px;
  }
  .card {
    width: 520px; height: 314px;
    background: var(--card);
    position: relative;
    overflow: hidden;
    box-shadow: 0 18px 40px rgba(0,0,0,.45);
  }

  /* Front */
  .card-front { display: flex; }
  .front-brand {
    width: 230px;
    display: flex; flex-direction: column; align-items: center; justify-content: center;
    gap: 18px;
  }
  .brand-dot {
    width: 120px; height: 120px; border-radius: 50%;
    background: var(--brand-blue);
  }
  .brand-name {
    color: var(--brand-blue);
    font-weight: 700;
    font-size: 17px;
    letter-spacing: .06em;
    text-transform: uppercase;
    text-align: center;
    line-height: 1.25;
  }
  .front-divider {
    width: 1px; background: var(--rule);
    margin: 56px 0;
  }
  .front-details {
    flex: 1;
    padding: 62px 0 0 28px;
  }
  .person-name {
    color: var(--brand-blue);
    font-weight: 700; font-size: 18px; letter-spacing: .03em;
    text-transform: uppercase;
  }
  .person-title {
    color: var(--ink-light);
    font-size: 14px; margin-top: 3px;
  }
  .contact-list { list-style: none; margin-top: 14px; }
  .contact-list li {
    display: flex; align-items: center; gap: 8px;
    color: var(--ink-light); font-size: 14px;
    margin-bottom: 6px;
  }
  .contact-list .gap { margin-top: 12px; }
  .contact-icon {
    width: 16px; height: 16px; flex: none;
  }
  .social-dot {
    width: 16px; height: 16px; flex: none; border-radius: 50%;
    background: var(--brand-blue);
  }

  /* Back */
  .card-back { display: flex; flex-direction: column; }
  .back-brand {
    height: 150px;
    display: flex; align-items: center; justify-content: center; gap: 16px;
  }
  .back-brand .brand-dot-small {
    width: 46px; height: 46px; border-radius: 50%;
    background: var(--silver);
  }
  .back-brand .brand-name {
    color: var(--silver);
    font-size: 22px; text-align: left;
  }
  .appointment-band {
    height: 110px;
    background: var(--band);
    padding: 22px 34px 0;
    color: var(--band-ink);
    font-weight: 700; font-size: 13px;
  }
  .write-line {
    display: flex; align-items: flex-end; gap: 6px; height: 26px;
  }
  .write-line .rule {
    flex: 1; border-bottom: 1px solid var(--band-ink); height: 1px;
  }
  .write-line + .write-line { margin-top: 20px; }
</style>
</head>
<body>
<main class="canvas">
  <section class="card card-front" aria-label="Business card front">
    <div class="front-brand">
      <div class="brand-dot"></div>
      <p class="brand-name">The Harbourline<br>Motion Clinic</p>
    </div>
    <div class="front-divider"></div>
    <div class="front-details">
      <h1 class="person-name">Daniel Carter</h1>
      <p class="person-title">Managing Director</p>
      <ul class="contact-list">
        <li>
          <svg class="contact-icon" viewBox="0 0 16 16" aria-hidden="true">
            <circle cx="8" cy="8" r="7.2" fill="none" stroke="var(--brand-blue)" stroke-width="1.4"/>
            <path d="M5.4 4.4l1.3-.3.8 1.9-.9.7c.4.9 1.1 1.6 2 2l.7-.9 1.9.8-.3 1.3c-2.9.2-5.7-2.6-5.5-5.5z" fill="var(--brand-blue)"/>
          </svg>
          402 318 7750
        </li>
        <li>
          <svg class="contact-icon" viewBox="0 0 16 16" aria-hidden="true">
            <circle cx="8" cy="8" r="8" fill="var(--brand-blue)"/>
            <rect x="4" y="5.2" width="8" height="5.6" fill="none" stroke="var(--card)" stroke-width="1.1"/>
            <path d="M4 5.4l4 3 4-3" fill="none" stroke="var(--card)" stroke-width="1.1"/>
          </svg>
          info@harbourlinemotion.com
        </li>
        <li class="gap"><span class="social-dot"></span>/harbourlinemotionclinic</li>
        <li><span class="social-dot"></span>@harbourlinemotionclinic</li>
      </ul>
    </div>
  </section>

  <section class="card card-back" aria-label="Business card back">
    <div class="back-brand">
      <div class="brand-dot-small"></div>
      <p class="brand-name">The Harbourline<br>Motion Clinic</p>
    </div>
    <div class="appointment-band">
      <div class="write-line"><span class="rule"></span></div>
      <div class="write-line">DATE<span class="rule"></span>TIME<span class="rule"></span></div>
    </div>
  </section>
</main>
</body>
</html>
```